New brand for digital company - your chance to get creative

We need to create a brand for our new business 'Lanternfield Digital'. Please read the brief below before progressing as we are looking for some quite specific outputs.

Background

We are positioning ourselves as ‘marketing technologists’ - we're helping businesses engage with their customers in the online space.

Our tactics include branding, marketing, online management, and social media, however we are differentiating ourselves by focusing on overall strategy, not just tactics. Our tagline is ‘Online made simple’.

We have stipulated some parameters for the brand but otherwise want designers to exercise their creativity.

Requirements
Must have
• We want to see an entire concept, not just a logo.

```html
<!DOCTYPE html>
<html lang="en">
<head>
<meta charset="utf-8">
<title>Lanternfield Digital – Online Made Simple</title>
<link href="https://fonts.googleapis.com/css2?family=Bebas+Neue&family=Arimo&display=swap" rel="stylesheet">
<style>
  :root {
    --brand-orange: #f7821b;
    --ink: #3d3d3d;
    --body-ink: #3a3a3a;
    --paper: #ffffff;
  }
  * { margin: 0; padding: 0; box-sizing: border-box; }
  html, body { width: 856px; height: 1200px; overflow: hidden; background: var(--paper); }
  .flyer { position: relative; width: 856px; height: 1200px; background: var(--paper); }

  .brand {
    position: absolute; top: 52px; left: 0; width: 856px;
    display: flex; justify-content: center; align-items: center; gap: 14px;
  }
  .brand-dot { width: 58px; height: 58px; border-radius: 50%; background: var(--brand-orange); }
  .brand-name {
    font-family: "Bebas Neue", sans-serif; font-size: 52px; line-height: 1;
    color: var(--brand-orange); letter-spacing: 1px;
  }

  .hero {
    position: absolute; top: 162px; left: 0; width: 856px; height: 438px;
    border-top: 6px solid var(--brand-orange); border-bottom: 7px solid var(--brand-orange);
  }
  .hero-photo {
    width: 100%; height: 100%;
    background:
      radial-gradient(ellipse 260px 180px at 22% 78%, rgba(235,235,228,0.95), transparent 70%),
      radial-gradient(ellipse 300px 260px at 80% 70%, rgba(25,30,30,0.95), transparent 75%),
      linear-gradient(160deg, #cfe3e9 0%, #9fc1cf 30%, #d9a86a 55%, #a8753e 75%, #2b2b28 100%);
  }

  .headline {
    position: absolute; top: 622px; left: 0; width: 856px; text-align: center;
    font-family: "Bebas Neue", sans-serif; font-size: 33px; line-height: 1;
    color: var(--ink); letter-spacing: 0.3px;
  }

  .body-copy {
    position: absolute; top: 683px; left: 37px; width: 780px; height: 425px;
    display: flex; justify-content: space-between;
  }
  .column {
    width: 380px; font-family: Arimo, Arial, sans-serif; font-size: 14.2px;
    line-height: 19px; color: var(--body-ink); text-align: justify;
  }
  .column p { text-indent: 50px; }
  .spacer-left { float: right; width: 1px; height: 78px; }
  .spacer-right { float: left; width: 1px; height: 78px; }
  .wrap-left {
    float: right; clear: right; width: 128px; height: 262px;
    shape-outside: circle(132px at 100% 50%);
  }
  .wrap-right {
    float: left; clear: left; width: 128px; height: 262px;
    shape-outside: circle(132px at 0 50%);
  }

  .ring { position: absolute; top: 762px; left: 302px; width: 252px; height: 252px; }

  .web-address {
    position: absolute; top: 1124px; left: 0; width: 856px; text-align: center;
    font-family: "Bebas Neue", sans-serif; font-size: 38px; line-height: 1;
    color: var(--brand-orange); letter-spacing: 0.5px;
  }
</style>
</head>
<body>
<main class="flyer">
  <header class="brand">
    <span class="brand-dot"></span>
    <span class="brand-name">Lanternfield Digital</span>
  </header>

  <section class="hero">
    <div class="hero-photo" role="img" aria-label="Photo of a young man working at a computer desk, mouse in the foreground"></div>
  </section>

  <h1 class="headline">‘Online made simple’ - we focus on overall strategy, not just tactics.</h1>

  <section class="body-copy">
    <div class="column">
      <div class="spacer-left"></div>
      <div class="wrap-left"></div>
      <p>Lorem ipsum dolor sit amet, consectetur adipiscing elit. Curabitur cursus placerat sapien in faucibus. Suspendisse ut dolor odio. Nunc ornare eleifend turpis vitae pellentesque. Vestibulum varius sodales libero, quis imperdiet orci ullamcorper a. Vestibulum vitae leo lectus. Aenean consequat ultricies suscipit. Aliquam sem sem, condimentum semper facilisis in, ornare eget enim. Nullam porta, ligula non laoreet lacinia, eros lacus faucibus leo, nec consectetur ligula elit sed ante. Proin nec tincidunt turpis. Etiam vitae dui erat. Nulla facilisi. Quisque auctor ante sed ligula luctus adipiscing. Morbi quis libero est. Aenean at velit nec ipsum posuere dictum. Ut tempor eros at libero molestie at varius lacus commodo. Maecenas vitae ante nunc. Ut tempor eros at libero molestie at varius lacus commodo. Lorem ipsum dolor sit amet, consectetur adipiscing elit. Curabitur cursus placerat sapien in faucibus. Suspendisse ut dolor odio.</p>
    </div>
    <div class="column">
      <div class="spacer-right"></div>
      <div class="wrap-right"></div>
      <p>Lorem ipsum dolor sit amet, consectetur adipiscing elit. Curabitur cursus placerat sapien in faucibus. Suspendisse ut dolor odio. Nunc ornare eleifend turpis vitae pellentesque. Vestibulum varius sodales libero, quis imperdiet orci ullamcorper a. Vestibulum vitae leo lectus. Aenean consequat ultricies suscipit. Aliquam sem sem, condimentum semper facilisis in, ornare eget enim. Nullam porta, ligula non laoreet lacinia, eros lacus faucibus leo, nec consectetur ligula elit sed ante. Proin nec tincidunt turpis. Etiam vitae dui erat. Nulla facilisi. Quisque auctor ante sed ligula luctus adipiscing. Morbi quis libero est. Aenean at velit nec ipsum posuere dictum. Ut tempor eros at libero molestie at varius lacus commodo. Maecenas vitae ante nunc. Ut tempor eros at libero molestie at varius lacus commodo. Lorem ipsum dolor sit amet, consectetur adipiscing elit. Curabitur cursus placerat sapien in faucibus. Suspendisse ut dolor odio.</p>
    </div>
  </section>

  <svg class="ring" viewBox="0 0 252 252" aria-hidden="true">
    <circle cx="126" cy="126" r="116" fill="none" stroke="var(--brand-orange)" stroke-width="9"/>
  </svg>

  <footer class="web-address">www.lanternfielddigital.com</footer>
</main>
</body>
</html>
```